New Business Card for our Indoor Golf Training Facility

We are looking for designs for a new business card for our indoor golf training facility. Attached is our logo, our logo with our slogan, and here is our elevator pitch (What makes us different from the others) not sure if all the info will fit on one card, maybe you can condense the elevator pitch? here is the info

Elevator Pitch
We work with serious golfers and those that want to be serious golfers…
to make you better, faster, at all phases of the game…
We use the same state-of-the-art technology as professional golfers…
which produces data sets that shows your improvement in real time.
Our facility is available 24/7 to our members, which allows you to improve on your time.

our website: www.brambleteegolf.com

Target Market(s)

Golfers

Font styles to use
Serif
Sans Serif

Colors
ec1f27
f59195
fbd4d5
919191
d3d3d3
1b1b1b

Requirements
Must have
• our logo or our logo with the slogan, elevator pitch (can be condensed or shortened)

```html
<!DOCTYPE html>
<html lang="en">
<head>
<meta charset="utf-8">
<title>Bramble Tee Golf – Business Card</title>
<link rel="stylesheet" href="https://fonts.googleapis.com/css2?family=Ubuntu:wght@400;500;700&family=Roboto:wght@400;500&display=swap">
<style>
  :root {
    --brand-red: #ec1f27;
    --soft-pink: #f59195;
    --pale-pink: #fbd4d5;
    --mid-grey: #919191;
    --light-grey: #d3d3d3;
    --ink: #1b1b1b;
    --white: #ffffff;
  }
  * { box-sizing: border-box; margin: 0; padding: 0; }
  html, body { width: 1200px; height: 900px; overflow: hidden; }
  body {
    background: var(--light-grey);
    font-family: "Ubuntu", "Roboto", sans-serif;
    position: relative;
  }
  .card {
    position: absolute;
    width: 620px;
    height: 354px;
    border-radius: 22px;
    overflow: hidden;
    box-shadow: 0 10px 30px rgba(27,27,27,0.25);
  }

  /* Shared brand lockup */
  .brand {
    display: flex;
    align-items: center;
    gap: 14px;
  }
  .brand__dot {
    border-radius: 50%;
    border: 5px solid currentColor;
    flex: none;
  }
  .brand__name {
    font-weight: 700;
    line-height: 1;
    white-space: nowrap;
  }
  .brand__slogan {
    font-weight: 400;
    margin-top: 6px;
    white-space: nowrap;
  }

  /* Back of card: pitch */
  .card--pitch {
    left: 110px; top: 60px;
    background: var(--brand-red);
    color: var(--white);
    text-align: center;
  }
  .card--pitch .brand { justify-content: center; margin-top: 52px; }
  .card--pitch .brand__dot { width: 62px; height: 62px; }
  .card--pitch .brand__name { font-size: 44px; }
  .card--pitch .brand__slogan { font-size: 15px; text-align: right; }
  .pitch { margin-top: 30px; padding: 0 30px; }
  .pitch__title {
    font-family: "Roboto", sans-serif;
    font-weight: 500;
    font-size: 17px;
    margin-bottom: 6px;
  }
  .pitch__text {
    font-family: "Roboto", sans-serif;
    font-size: 13px;
    line-height: 1.55;
  }

  /* Front of card: contact */
  .card--contact {
    left: 470px; top: 480px;
    background: var(--white);
  }
  .card__wave { position: absolute; inset: 0; }
  .person {
    position: absolute;
    right: 40px; top: 20px;
    text-align: right;
    color: var(--brand-red);
  }
  .person__name { font-size: 30px; font-weight: 500; line-height: 1.15; }
  .person__role { font-size: 15px; margin-top: 2px; }
  .card--contact .brand {
    position: absolute;
    left: 30px; top: 130px;
    gap: 12px;
    color: var(--brand-red);
  }
  .card--contact .brand__dot { width: 52px; height: 52px; border-width: 4px; }
  .card--contact .brand__name { font-size: 32px; }
  .card--contact .brand__slogan { font-size: 13px; }
  .contact {
    position: absolute;
    right: 26px; bottom: 24px;
    color: var(--white);
    font-size: 13px;
    line-height: 1.5;
    text-align: right;
    list-style: none;
  }
  .contact li { display: flex; align-items: center; justify-content: flex-end; gap: 8px; }
  .contact svg { width: 12px; height: 12px; flex: none; }
  .contact .contact__address { padding-right: 20px; margin-top: 4px; }
</style>
</head>
<body>

<section class="card card--pitch">
  <div class="brand">
    <span class="brand__dot"></span>
    <div>
      <div class="brand__name">Bramble Tee Golf</div>
      <div class="brand__slogan">Play Well. Play Often. Be Better.</div>
    </div>
  </div>
  <div class="pitch">
    <h2 class="pitch__title">Elevator Pitch</h2>
    <p class="pitch__text">
      We work with serious golfers and those that want to be serious golfers…<br>
      to make you better, faster, at all phases of the game…<br>
      We use the same state-of-the-art technology as professional golfers…<br>
      which produces data sets that shows your improvement in real time.<br>
      Our facility is available 24/7 to our members, which allows you to improve on your time.
    </p>
  </div>
</section>

<section class="card card--contact">
  <svg class="card__wave" viewBox="0 0 620 354" aria-hidden="true">
    <path d="M0 290 C220 285 350 272 395 205 C435 140 520 125 620 120 L620 354 L0 354 Z" fill="var(--brand-red)"/>
    <path d="M0 312 C230 307 370 294 415 224 C455 160 535 145 620 140" fill="none" stroke="var(--white)" stroke-width="3"/>
    <path d="M120 268 C290 260 345 240 372 190 C405 125 510 100 620 95" fill="none" stroke="var(--brand-red)" stroke-width="5"/>
  </svg>

  <div class="person">
    <div class="person__name">Daniel Reyes</div>
    <div class="person__role">Director</div>
  </div>

  <div class="brand">
    <span class="brand__dot"></span>
    <div>
      <div class="brand__name">Bramble Tee Golf</div>
      <div class="brand__slogan">Play Well. Play Often. Be Better.</div>
    </div>
  </div>

  <ul class="contact">
    <li>555-310-2846
      <svg viewBox="0 0 24 24" fill="currentColor"><path d="M6.6 10.8a15 15 0 0 0 6.6 6.6l2.2-2.2c.3-.3.7-.4 1-.2 1.1.4 2.3.6 3.6.6.6 0 1 .4 1 1V20c0 .6-.4 1-1 1A17 17 0 0 1 3 4c0-.6.4-1 1-1h3.5c.6 0 1 .4 1 1 0 1.3.2 2.5.6 3.6.1.3 0 .7-.2 1z"/></svg>
    </li>
    <li>info@brambleteegolf.com
      <svg viewBox="0 0 24 24" fill="none" stroke="currentColor" stroke-width="2.5"><rect x="3" y="5" width="18" height="14" rx="2"/><path d="M3 7l9 6 9-6"/></svg>
    </li>
    <li>www.brambleteegolf.com
      <svg viewBox="0 0 24 24" fill="none" stroke="currentColor" stroke-width="2.2"><circle cx="12" cy="12" r="9"/><path d="M3 12h18M12 3c3 3 3 15 0 18M12 3c-3 3-3 15 0 18"/></svg>
    </li>
    <li class="contact__address">1840 W. Alder Rd. Unit B4<br>Fairhaven, OH 45012</li>
  </ul>
</section>

</body>
</html>
```